Korvex App's Dashboard Redesign

We are redesigning our existing Korvex app (http://www.tamselo.com) to use Korvex's new Plinth Layout guidelines (read more here: http://www.brindlework.com/design/).

We would like to see new designs of the app's main screen (see tamselo_dashboard.png) from you.

The new dashboard screen design should:
A. follow Korvex's new Plinth Layout guidelines
B. contain an actionbar at the top (with an icon for hints and a "hamburger menu icon" on the left)
C. contain 4 buttons to the app's other screens: 1. Edit today's symptoms, 2. Calendar view, 3. Timeline view, 4. Chart view. (Please, do not put the buttons into tabs, as we want to avoid putting tabs on other screens too)
D. keep the basic concept of the cycle wheel (circle/donut representing the days of cycle; distinguish passed/upcoming days of cycle; show current cycle day; show menses days/fertile days/ovulation day)
E. contain iconic or textual predictions of the number of days to the next menses/ovulation
F. be easily themable to different colors (as the app supports more color themes)

To get a better idea about the app in general and the dashboard/cycle wheel in particular, please install the app and read Petal Loop Guides. This will help you understand the functional requirements.

Wheel

```html
<!DOCTYPE html>
<html lang="en">
<head>
<meta charset="utf-8">
<title>Korvex Dashboard — Cycle Wheel</title>
<link rel="stylesheet" href="https://fonts.googleapis.com/css2?family=Roboto:wght@100;700&display=swap">
<style>
  :root {
    --stage: #5d5d5d;
    --tile: #6b6b6b;
    --status-bar: #b862ae;
    --action-bar: #cf8ec4;
    --screen: #e1b8da;
    --wheel-track: #cf8ec4;
    --menses: #ff2a1f;
    --fertile: #0db34a;
    --ink-light: #f5e1f0;
    --frame: #2a2a2a;
  }
  * { box-sizing: border-box; margin: 0; padding: 0; }
  html, body { width: 1200px; height: 975px; overflow: hidden; }
  body {
    background: var(--stage);
    font-family: "Roboto", Arial, sans-serif;
    position: relative;
  }
  .phone {
    position: absolute;
    left: 47px; top: 37px;
    width: 601px; height: 902px;
    background: var(--screen);
    border: 1px solid var(--frame);
    overflow: hidden;
  }
  .status-bar { height: 30px; background: var(--status-bar); }
  .action-bar {
    height: 92px;
    background: var(--action-bar);
    position: relative;
  }
  .action-bar svg {
    position: absolute;
    top: 24px;
    width: 60px; height: 45px;
    overflow: visible;
  }
  .cycle-wheel {
    position: absolute;
    left: 0; top: 0;
    width: 600px; height: 900px;
  }
  .cycle-day {
    position: absolute;
    left: 0; width: 600px;
    top: 412px;
    text-align: center;
    font-weight: 100;
    font-size: 158px;
    line-height: 1;
    color: var(--ink-light);
    letter-spacing: -2px;
  }
  .legend {
    position: absolute;
    left: 722px; top: 38px;
    list-style: none;
  }
  .legend li {
    display: flex;
    align-items: center;
    height: 89px;
    margin-bottom: 31px;
  }
  .legend-tile {
    width: 120px; height: 89px;
    background: var(--tile);
    flex: none;
    overflow: visible;
  }
  .legend-label {
    margin-left: 45px;
    font-weight: 700;
    font-size: 24px;
    color: var(--ink-light);
  }
  .legend-label.is-menses { color: var(--menses); }
</style>
</head>
<body>

<main class="phone" aria-label="Dashboard screen">
  <div class="status-bar"></div>
  <nav class="action-bar" aria-label="Action bar">
    <svg style="left:29px" viewBox="0 0 85 63" aria-label="Menu"><g stroke="var(--ink-light)" stroke-width="4"><line x1="9" y1="10" x2="75" y2="10"/><line x1="9" y1="30" x2="75" y2="30"/><line x1="9" y1="50" x2="75" y2="50"/></g></svg>
    <svg style="left:150px" viewBox="0 0 85 63" aria-label="Edit today's symptoms"><g stroke="var(--ink-light)" stroke-width="4" fill="none"><line x1="9" y1="10" x2="66" y2="10"/><line x1="9" y1="25" x2="66" y2="25"/><line x1="9" y1="40" x2="40" y2="40"/><polyline points="50,42 60,52 84,30"/></g></svg>
    <svg style="left:272px" viewBox="0 0 85 63" aria-label="Chart view"><g stroke="var(--ink-light)" stroke-width="4" fill="none"><line x1="12" y1="0" x2="12" y2="63"/><line x1="0" y1="48" x2="75" y2="48"/><polyline points="20,40 38,22 50,32 72,12"/></g></svg>
    <svg style="left:395px" viewBox="0 0 85 63" aria-label="Calendar view"><g fill="var(--ink-light)"><rect x="22" y="2" width="4" height="10"/><rect x="59" y="2" width="4" height="10"/><rect x="10" y="9" width="65" height="5"/><rect x="10" y="18" width="65" height="44"/></g></svg>
    <svg style="left:524px" viewBox="0 0 85 63" aria-label="Timeline view"><g stroke="var(--ink-light)" stroke-width="4" fill="none"><rect x="8" y="12" width="68" height="40"/><line x1="50" y1="0" x2="50" y2="63"/></g></svg>
  </nav>

  <svg class="cycle-wheel" viewBox="0 0 600 900" role="img" aria-label="Cycle wheel, day 28, menses and fertile days">
    <polygon points="278,204 324,204 301,232" fill="var(--ink-light)"/>
    <circle cx="300" cy="511" r="234" fill="none" stroke="var(--wheel-track)" stroke-width="44"/>
    <circle cx="300" cy="511" r="234" fill="none" stroke="var(--menses)" stroke-width="44"
            stroke-dasharray="457 1013" transform="rotate(-90 300 511)"/>
    <circle cx="300" cy="511" r="234" fill="none" stroke="var(--fertile)" stroke-width="44"
            stroke-dasharray="229 1241" transform="rotate(137 300 511)"/>
    <polyline points="235,596 252,612 287,580" fill="none" stroke="var(--fertile)" stroke-width="8" stroke-linecap="round" stroke-linejoin="round"/>
    <g fill="var(--menses)">
      <path transform="translate(313 574) scale(1.5)" d="M5 0C5 0 0 6 0 9a5 5 0 0 0 10 0C10 6 5 0 5 0Z"/>
      <path transform="translate(329 575) scale(2.7)" d="M5 0C5 0 0 6 0 9a5 5 0 0 0 10 0C10 6 5 0 5 0Z"/>
    </g>
  </svg>
  <div class="cycle-day">28</div>
</main>

<ul class="legend" aria-label="Icon key">
  <li>
    <svg class="legend-tile" viewBox="0 0 85 63"><g stroke="var(--ink-light)" stroke-width="4"><line x1="9" y1="10" x2="75" y2="10"/><line x1="9" y1="30" x2="75" y2="30"/><line x1="9" y1="50" x2="75" y2="50"/></g></svg>
    <span class="legend-label">“Hamburger” icon</span>
  </li>
  <li>
    <svg class="legend-tile" viewBox="0 0 85 63"><g stroke="var(--ink-light)" stroke-width="4" fill="none"><line x1="9" y1="10" x2="66" y2="10"/><line x1="9" y1="25" x2="66" y2="25"/><line x1="9" y1="40" x2="40" y2="40"/><polyline points="50,42 60,52 84,30"/></g></svg>
    <span class="legend-label">Symptoms icon</span>
  </li>
  <li>
    <svg class="legend-tile" viewBox="0 0 85 63"><g stroke="var(--ink-light)" stroke-width="4" fill="none"><line x1="12" y1="0" x2="12" y2="63"/><line x1="0" y1="48" x2="75" y2="48"/><polyline points="20,40 38,22 50,32 72,12"/></g></svg>
    <span class="legend-label">Chart view icon</span>
  </li>
  <li>
    <svg class="legend-tile" viewBox="0 0 85 63"><g fill="var(--ink-light)"><rect x="22" y="2" width="4" height="10"/><rect x="59" y="2" width="4" height="10"/><rect x="10" y="9" width="65" height="5"/><rect x="10" y="18" width="65" height="44"/></g></svg>
    <span class="legend-label">Calendar view icon</span>
  </li>
  <li>
    <svg class="legend-tile" viewBox="0 0 85 63"><g stroke="var(--ink-light)" stroke-width="4" fill="none"><rect x="8" y="12" width="68" height="40"/><line x1="50" y1="0" x2="50" y2="63"/></g></svg>
    <span class="legend-label">Timeline view icon</span>
  </li>
  <li>
    <svg class="legend-tile" viewBox="0 0 85 63"><polygon points="9,10 75,10 42,52" fill="var(--ink-light)"/></svg>
    <span class="legend-label">Indicator arrow</span>
  </li>
  <li>
    <svg class="legend-tile" viewBox="0 0 85 63"><g fill="var(--menses)"><path transform="translate(8 2) scale(1.5)" d="M5 0C5 0 0 6 0 9a5 5 0 0 0 10 0C10 6 5 0 5 0Z"/><path transform="translate(30 2) scale(3)" d="M5 0C5 0 0 6 0 9a5 5 0 0 0 10 0C10 6 5 0 5 0Z"/></g></svg>
    <span class="legend-label is-menses">Menses days</span>
  </li>
</ul>

</body>
</html>
```